Zielgruppe
Wir sind ein Online Shop und vertreiben verschiedene Lacke zur Sanierung von Fliesen, Küchenmöbeln, Badewannen usw.
www.lurno-buntwerk.de
Jetzt benötigen wir einen Flyer für die Küchenmöbellacke.
DIN lang (105 x 210 mm) hoch / 4 Seiten
Sind in der Größe aber nicht festgelegt.
Alle Info´s die Sie benötigen finden Sie unter:
https://www.lurno-buntwerk.com/farben-lacke/kuechenmoebellack/
https://www.lurno-buntwerk.com/pdf/Technisches-Datenblatt-KUECHENMOEBELLACK.pdf
Wir haben von zwei Kunden Vorher - Nachher Bilder die Sie vielleicht verwenden können.
Wenn Sie noch Informationen benötigen sprechen Sie micht an.
Ich freue mich auf viele, schöne Kreative Vorschläge.
Aufgabenstellung
Der Flyer ansprechend, frisch und zeitgemäß gestaltet sein.

```html
<!DOCTYPE html>
<html lang="de">
<head>
<meta charset="utf-8">
<title>Verarbeitungshinweise – Küchenmöbellack</title>
<link rel="stylesheet" href="https://fonts.googleapis.com/css2?family=Arimo:ital,wght@0,400;0,700;1,700&display=swap">
<style>
  :root {
    --salmon: #f4a99f;
    --magenta: #fe2360;
    --panel: rgba(255, 250, 249, 0.86);
    --ink-green: #3ee83a;
    --ink-blue: #2f3ff0;
    --ink-cyan: #3fe9e6;
    --ink-violet: #8a3cf0;
    --ink-red: #ff4a2a;
    --ink-pink: #ff3fa0;
    --lizard: #4fb68f;
  }
  html, body {
    margin: 0;
    padding: 0;
    width: 1200px;
    height: 2400px;
    overflow: hidden;
  }
  .flyer-page {
    position: relative;
    width: 1200px;
    height: 2400px;
    background: var(--salmon);
    overflow: hidden;
    font-family: "Arimo", Arial, sans-serif;
    color: var(--magenta);
  }
  .ink-clouds {
    position: absolute;
    inset: 0;
  }
  .ink-clouds svg { width: 100%; height: 100%; display: block; }
  .page-title {
    position: absolute;
    left: 68px;
    top: 42px;
    margin: 0;
    font-size: 116px;
    line-height: 123px;
    font-weight: 700;
    font-style: italic;
    letter-spacing: -1px;
    color: var(--magenta);
  }
  .mascot-photo {
    position: absolute;
    left: 700px;
    top: 135px;
    width: 500px;
    height: 185px;
    border-radius: 50% 40% 30% 50% / 60% 50% 40% 50%;
    background: radial-gradient(ellipse at 30% 40%, #e6c23a 0%, var(--lizard) 35%, #2f8fa0 75%, rgba(79,182,143,0) 100%);
  }
  .info-panel {
    position: absolute;
    left: 70px;
    top: 315px;
    width: 1061px;
    height: 2018px;
    background: var(--panel);
    box-sizing: border-box;
    padding: 36px 40px 0 51px;
  }
  .info-section { margin: 0 0 38.7px; }
  .info-heading {
    margin: 0;
    font-size: 29px;
    line-height: 38.7px;
    font-weight: 700;
    letter-spacing: 0.2px;
  }
  .info-text {
    margin: 0;
    font-size: 29px;
    line-height: 38.7px;
    font-weight: 400;
  }
</style>
</head>
<body>
<main class="flyer-page">
  <div class="ink-clouds" role="img" aria-label="Bunte Farbwolken aus Tinte in Grün, Blau, Violett, Rot und Pink an den Rändern">
    <svg viewBox="0 0 1200 2400" preserveAspectRatio="none">
      <defs>
        <linearGradient id="inkLeft" x1="0" y1="0" x2="0" y2="1">
          <stop offset="0" stop-color="var(--ink-green)"/>
          <stop offset="0.2" stop-color="#1d3b2a"/>
          <stop offset="0.4" stop-color="var(--ink-blue)"/>
          <stop offset="0.55" stop-color="var(--ink-green)"/>
          <stop offset="0.8" stop-color="var(--ink-cyan)"/>
          <stop offset="1" stop-color="var(--ink-blue)"/>
        </linearGradient>
        <linearGradient id="inkRight" x1="0" y1="0" x2="0" y2="1">
          <stop offset="0" stop-color="var(--ink-violet)"/>
          <stop offset="0.25" stop-color="var(--ink-red)"/>
          <stop offset="0.45" stop-color="var(--ink-pink)"/>
          <stop offset="0.65" stop-color="var(--ink-blue)"/>
          <stop offset="0.85" stop-color="var(--ink-violet)"/>
          <stop offset="1" stop-color="var(--ink-pink)"/>
        </linearGradient>
        <linearGradient id="inkBottom" x1="0" y1="0" x2="1" y2="0">
          <stop offset="0" stop-color="var(--ink-cyan)"/>
          <stop offset="0.5" stop-color="#3a55c8"/>
          <stop offset="1" stop-color="var(--ink-pink)"/>
        </linearGradient>
      </defs>
      <path d="M0 680 C60 700 90 760 80 820 L80 2400 L0 2400 Z" fill="url(#inkLeft)"/>
      <path d="M1200 470 C1150 500 1120 560 1125 620 L1125 2400 L1200 2400 Z" fill="url(#inkRight)"/>
      <rect x="0" y="2325" width="1200" height="75" fill="url(#inkBottom)"/>
    </svg>
  </div>

  <h1 class="page-title">Verarbeitungs-<br>hinweise:</h1>

  <div class="mascot-photo" role="img" aria-label="Foto eines bunten Chamäleons, das auf dem Textfeld sitzt"></div>

  <section class="info-panel">
    <div class="info-section">
      <h2 class="info-heading">UNTERGRUNDVORBEHANDLUNG:</h2>
      <p class="info-text">Der Untergrund muss sauber, trocken, öl-, fettfrei und tragfähig<br>sein. Er sollte dem weiteren Verwendungszweck entsprechend vor-<br>grundiert werden. Altanstriche anschleifen/anstrahlen, wenn er-<br>forderlich entfernen. Optimale Reinigung der Oberflächen mit LUR-<br>NO Vorbehandlung Nr. 328 (im Lieferumfang enthalten). Vor dem<br>Lackieren sollten Möbelgriffe oder sonstige Applikationen ent-<br>fernt werden.</p>
    </div>
    <div class="info-section">
      <h2 class="info-heading">REINIGUNG DER ARBEITSGERÄTE:</h2>
      <p class="info-text">Die Reinigung erfolgt grundsätzlich mit Wasser. Nach Antrockung<br>ist das wasserverdünnbare Material nicht mehr wasserlöslich.</p>
    </div>
    <div class="info-section">
      <h2 class="info-heading">VERDÜNNUNG:</h2>
      <p class="info-text">Verdünnung zum Einstellen der Viskosität beim Spritzen oder zum<br>Reinigen der Arbeitsgeräte: Wasser</p>
    </div>
    <div class="info-section">
      <h2 class="info-heading">VERARBEITUNGSZEIT:</h2>
      <p class="info-text">ca. 4 Stunden / 20 °C, innerhalb der 4 Stunden kann mit Wasser<br>nachverdünnt werden, damit ein einheitlicher Farbverlauf gewähr-<br>leistet ist. Nach Ablauf der 4 Stunden ist die Farbe nicht mehr ver-<br>arbeitbar. Nach Einrühren des Härters darf die Dose nicht mehr ge-<br>schlossen werden!</p>
    </div>
    <div class="info-section">
      <h2 class="info-heading">VERARBEITUNGSTEMPERATUR:</h2>
      <p class="info-text">min. 8°C, min. + 3°C oberhalb der Taupunktgrenze</p>
    </div>
    <div class="info-section">
      <h2 class="info-heading">APPLIKATIONSDATEN:</h2>
      <p class="info-text">Zunächst muss die Farbe gründlich durchgerührt werden, bis eine<br>homogene Mischung erfolgt ist (idealerweise mit einem Elektroüh-<br>rer). Erst danach wird der mitgelieferte Härter vollständig in die Far-<br>be eingerührt. Bei der Verarbeitung im Streich- bzw. Rollverfahren<br>ist der Beschichtungsstoff gleichmäßig aufzutragen. Für das Roll-<br>verfahren sollten velourbeflockte Lackwalzen (im Lieferumfang ent-<br>halten) eingesetzt werden.</p>
    </div>
    <div class="info-section">
      <h2 class="info-heading">VERARBEITUNG:</h2>
      <p class="info-text">Rollen, Streichen und verschiedene Spritzverfahren.</p>
    </div>
    <div class="info-section">
      <h2 class="info-heading">TROCKNUNG:</h2>
      <p class="info-text">bei 20°c / 65% rel. Luftfeuchtigkeit staubtrocken nach ca. 45 min<br>abhängig von der Nassschichtdicke, Grifffesttrocknung nach ca. 3<br>Stunden abhängig von der Nassschichtdicke. Komplett durchge-<br>trocknet und voll belastbar nach 5 Tagen.</p>
    </div>
    <div class="info-section">
      <h2 class="info-heading">ÜBERSTREICHBAR:</h2>
      <p class="info-text">nach 12 Stunden</p>
    </div>
    <div class="info-section">
      <h2 class="info-heading">SCHLEIFBAR:</h2>
      <p class="info-text">nach 12 Stunden</p>
    </div>
  </section>
</main>
</body>
</html>
```